" Somos uma empresa que faz o gerenciamento de um condomínio auxiliando o síndico, sub síndico e conselheiros. Temos contato mais próximo ao síndico, por este motivo ele é o nosso principal cliente. Na prática, efetuamos todo o serviço administrativo e burocrático para o condomínio, desde geração da receita até o pagamento das despesas do condomínio. Também fazemos gestão de RH para os funcionários do condomínio. Atualmente temos 330 condomínios, internamente temos 80 funcionários e 3 escritórios. Nesse outdoor, precisa deixar claro que a empresa Marzolo Condomínios está completando 30 anos de experiência, e atualmente tem uma nova sede no bairro da praia das Astúrias. Somos uma empresa na cidade de Guarujá. SP. Condomínios de veraneio é o nosso forte. "

```html
<!DOCTYPE html>
<html lang="pt-BR">
<head>
<meta charset="utf-8">
<title>Marzolo Condomínios — Banner</title>
<link rel="stylesheet" href="https://fonts.googleapis.com/css2?family=Roboto+Condensed:wght@700&family=Tinos&display=swap">
<style>
  :root {
    --page-bg: #eef1f2;
    --banner-blue: #22618c;
    --white: #ffffff;
    --green: #3dbb6a;
    --teal: #1aa3a7;
    --photo-light: #e9e4de;
    --photo-mid: #c9c0b6;
    --photo-dark: #8a7f76;
  }
  * { margin: 0; padding: 0; box-sizing: border-box; }
  html, body { width: 1200px; height: 1200px; overflow: hidden; }
  body { background: var(--page-bg); position: relative; }

  .banner {
    position: absolute; left: 30px; top: 408px;
    width: 1140px; height: 383px;
    background: var(--banner-blue);
    overflow: hidden;
  }
  .banner-shapes { position: absolute; inset: 0; width: 100%; height: 100%; }

  .headline {
    position: absolute; left: 667px; top: 22px;
    font-family: "Roboto Condensed", sans-serif; font-weight: 700;
    color: var(--white);
    font-size: 42px; line-height: 1.0; letter-spacing: 0.2px;
  }
  .headline .tagline { display: block; font-size: 26px; margin-top: 4px; }

  .brand {
    position: absolute; left: 990px; top: 22px; width: 120px;
    text-align: center; color: var(--white);
    font-family: "Roboto Condensed", sans-serif; font-weight: 700;
  }
  .brand-square { width: 80px; height: 80px; margin: 0 auto 8px; background: var(--white); }
  .brand-name { font-size: 20px; line-height: 1.05; }
  .brand-name small { display: block; font-size: 11px; letter-spacing: 1.5px; }

  .intro {
    position: absolute; left: 667px; top: 168px; width: 440px;
    font-family: "Tinos", serif; color: var(--white);
    font-size: 25px; line-height: 1.2;
  }

  .contact {
    position: absolute; left: 770px; top: 282px; width: 230px;
    text-align: center; color: var(--white);
    font-family: "Roboto Condensed", sans-serif; font-weight: 700;
  }
  .contact-label { font-size: 17px; letter-spacing: 0.5px; margin-bottom: 2px; }
  .contact-line { display: flex; align-items: center; justify-content: center; gap: 8px; font-size: 27px; line-height: 1.1; }
  .contact-icon { width: 20px; height: 20px; flex: none; }
</style>
</head>
<body>
  <section class="banner">
    <svg class="banner-shapes" viewBox="0 0 1140 383" aria-hidden="false">
      <defs>
        <linearGradient id="photoTone" x1="0" y1="0" x2="1" y2="1">
          <stop offset="0" stop-color="var(--photo-light)"/>
          <stop offset="0.55" stop-color="var(--photo-mid)"/>
          <stop offset="1" stop-color="var(--photo-dark)"/>
        </linearGradient>
      </defs>
      <path class="swoosh-teal" d="M640 0 C 610 130, 560 270, 470 383 H505 C 600 270, 650 130, 680 0 Z" fill="var(--teal)"/>
      <path class="swoosh-white" d="M595 0 C 565 130, 515 270, 425 383 H478 C 570 270, 620 130, 648 0 Z" fill="var(--white)"/>
      <path class="swoosh-green" d="M560 0 C 545 60, 530 110, 510 160 C 540 110, 565 60, 595 0 Z" fill="var(--green)"/>
      <path class="family-photo" role="img" aria-label="Foto de família sorridente: mãe, filha e pai abraçados"
            d="M0 0 H590 C 560 130, 510 270, 420 383 H0 Z" fill="url(#photoTone)"/>
      <path class="corner-green" d="M0 0 H110 C 70 20, 30 45, 0 75 Z" fill="var(--green)"/>
      <path class="corner-white" d="M0 0 H75 C 45 15, 20 35, 0 55 Z" fill="var(--white)"/>
      <path class="corner-teal" d="M0 0 H45 C 28 10, 12 22, 0 34 Z" fill="var(--teal)"/>
    </svg>

    <h1 class="headline">É tranquilidade<br>que você quer?<span class="tagline">Então deixa com a gente.</span></h1>

    <div class="brand">
      <div class="brand-square"></div>
      <div class="brand-name">MARZOLO<small>CONDOMÍNIOS</small></div>
    </div>

    <p class="intro">Uma empresa inovadora, com 30 anos de experiência, focada em soluções práticas e atendimento rápido.</p>

    <div class="contact">
      <div class="contact-label">FALE COM A GENTE</div>
      <div class="contact-line">
        <svg class="contact-icon" viewBox="0 0 24 24"><path fill="var(--white)" d="M6.6 10.8a15.1 15.1 0 0 0 6.6 6.6l2.2-2.2a1 1 0 0 1 1-.25 11.4 11.4 0 0 0 3.6.57 1 1 0 0 1 1 1V20a1 1 0 0 1-1 1A17 17 0 0 1 3 4a1 1 0 0 1 1-1h3.5a1 1 0 0 1 1 1c0 1.25.2 2.45.57 3.57a1 1 0 0 1-.25 1z"/></svg>
        <span>(13) 3210-4500</span>
      </div>
      <div class="contact-line">
        <svg class="contact-icon" viewBox="0 0 24 24"><circle cx="12" cy="12" r="10" fill="var(--white)"/></svg>
        <span>(13) 98741-2256</span>
      </div>
    </div>
  </section>
</body>
</html>
```